Australian Real Estate Sales Consultant needs web design please.

I am a female residential real estate sales consultant for a large australian real estate franchise.
I need a web design for "wordpress" that contains an area that will accommodate my photo and details and company logo.
A large area that contains a feature property where images are on something like a slide show.
Tabs or something similar with images for Selling, Sold, Photography and News where people can look at listings but I do not want people to be able to post a comment.
Reason: Need more designers, may be forced to change to wordpress and offer more money.
Reason: Sorry for the delay, I have been concentrating on another project which I needed completed. I am now able to focus on my web design project and hope to have it all set up in the next 10 days as it is a high priority for me. Thank you for your patience and I will begin providing feedback to your designs shortly. Thanks, Marisska.
Target Market(s)
Potential sellers or purchasers of residential property
Industry/Entity Type
Residential
Requirements
Must have
- Ease of changing property photos and info
Nice to have
- Bright attractive colours

```html
<!DOCTYPE html>
<html lang="en">
<head>
<meta charset="utf-8">
<title>Coastline Realty – Sales Consultant</title>
<link href="https://fonts.googleapis.com/css2?family=EB+Garamond:wght@700&family=Arimo:ital,wght@0,400;0,700;1,700&display=swap" rel="stylesheet">
<style>
:root{
  --navy:#0b3a78;
  --navy-dark:#072a5a;
  --red:#d9161c;
  --red-dark:#a80f14;
  --hero-bg:#dde3ec;
  --text:#3c3c3c;
  --muted:#6f6f6f;
  --date-bg:#ead9b3;
  --footer:#7b1d22;
  --white:#ffffff;
}
*{margin:0;padding:0;box-sizing:border-box}
html,body{width:1200px;height:1200px;overflow:hidden;background:#f6f6f6}
body{position:relative;font-family:"Arimo",Arial,sans-serif;color:var(--text)}
.abs{position:absolute}

.site-header{left:0;top:0;width:1200px;height:107px;background:linear-gradient(#0e4286,var(--navy-dark))}
.brand{left:77px;top:36px;display:flex;align-items:center;gap:12px;color:var(--white);font-weight:700;font-size:34px;letter-spacing:.5px}
.brand-square{width:26px;height:26px;background:var(--red)}
.main-nav{right:77px;top:54px;display:flex;gap:36px;font-size:18px;color:var(--white)}

.hero{left:0;top:107px;width:1200px;height:429px;background:repeating-linear-gradient(0deg,#e3e8f0 0 3px,#d7dde8 3px 5px)}
.feature-photo{left:77px;top:147px;width:712px;height:359px;background:var(--white);padding:9px;box-shadow:0 2px 5px rgba(0,0,0,.2)}
.feature-photo .fill{width:100%;height:100%;background:linear-gradient(#8a9aa8 0%,#b8b8b0 45%,#8c8070 70%,#4f7a3a 100%)}
.new-ribbon{left:68px;top:136px}
.slide-prev,.slide-next{top:482px;width:32px;height:30px;border-radius:4px}
.slide-prev{left:695px;background:#6f747a}
.slide-next{left:735px;background:var(--red)}
.hero-title{left:805px;top:152px;width:330px;font-family:"EB Garamond",Georgia,serif;font-weight:700;font-size:35px;line-height:38px;color:var(--navy)}
.hero-copy{left:805px;top:232px;width:322px;font-style:italic;font-weight:700;font-size:15.5px;line-height:24px;color:#444}
.btn{display:flex;align-items:center;justify-content:center;color:var(--white);font-weight:700;font-size:16px;border-radius:3px}
.btn-learn{left:833px;top:453px;width:254px;height:46px;background:linear-gradient(var(--red),var(--red-dark))}

.agent-photo{left:79px;top:569px;width:134px;height:148px;background:var(--white);padding:4px;box-shadow:0 1px 3px rgba(0,0,0,.3)}
.agent-photo .fill{width:100%;height:100%;background:linear-gradient(#d8d8d8,#8a6f60 55%,#2a2224)}
.agent-bio{left:236px;top:570px;width:870px;font-size:15px;line-height:24px}
.divider{left:77px;top:735px;width:1046px;border-top:1px dotted #c8c8c8}

.section-title{font-size:25px;color:var(--muted)}
.proposals-title{left:77px;top:748px}
.news-title{left:819px;top:748px}
.thumb{width:134px;height:124px;background:var(--white);padding:3px;box-shadow:0 1px 3px rgba(0,0,0,.25)}
.thumb .fill{width:100%;height:100%;background:linear-gradient(#e6e2d8,#c9c0a8 60%,#9a8f78)}
.btn-navy{background:linear-gradient(#134a92,var(--navy-dark));font-size:16px}
.btn-proposals{left:522px;top:1082px;width:181px;height:36px}
.btn-news{left:1017px;top:1082px;width:108px;height:36px}

.date{left:817px;width:63px;height:68px;background:var(--date-bg);color:var(--red);text-align:center;font-weight:700}
.date .day{display:block;font-size:28px;line-height:36px;padding-top:4px}
.date .mon{display:block;font-size:15px}
.news-text{left:903px;width:218px;font-size:14px;line-height:24px}

.site-footer{left:0;top:1148px;width:1200px;height:52px;background:var(--footer)}
.copyright{left:82px;top:1163px;font-size:13px;color:#f1dede}
.social{top:1160px;width:26px;height:26px;border-radius:3px}
</style>
</head>
<body>
<header class="abs site-header"></header>
<div class="abs brand"><span class="brand-square"></span>Coastline Realty</div>
<nav class="abs main-nav"><span>HOME</span><span>SELLING</span><span>SOLD</span><span>PHOTOGRAPHY</span><span>NEWS</span></nav>

<section class="abs hero"></section>
<div class="abs feature-photo"><div class="fill" role="img" aria-label="Featured property photo: two-storey stone and siding family home with lawn"></div></div>
<svg class="abs new-ribbon" width="156" height="156" viewBox="0 0 156 156">
  <path d="M0 0 H156 L0 156 Z" fill="#d9161c"/>
  <text x="42" y="62" transform="rotate(-45 42 62)" fill="#fff" font-family="Arimo,Arial,sans-serif" font-weight="700" font-size="20" text-anchor="middle">NEW</text>
</svg>
<svg class="abs slide-prev" viewBox="0 0 32 30"><path d="M19 9 L12 15 L19 21 Z" fill="#fff"/></svg>
<svg class="abs slide-next" viewBox="0 0 32 30"><path d="M13 9 L20 15 L13 21 Z" fill="#fff"/></svg>
<h1 class="abs hero-title">LOREM IPSUM DOLOR SIT AMET,</h1>
<p class="abs hero-copy">Lorem ipsum dolor sit amet, consectetuer adipiscing elit. Aenean commodo ligula eget dolor. Aenean massa. Cum sociis natoque penatibus et magnis diCum sociis natoque penatibus et magnis dis parturient montes, nascetur ridLorem ipsum parturient montes, nascetur ridLorem ipsum dolor sit amet, consectetuer adipiscing elit.</p>
<a class="abs btn btn-learn">CLICK HERE TO LEARN MORE</a>

<div class="abs agent-photo"><div class="fill" role="img" aria-label="Portrait of the sales consultant"></div></div>
<p class="abs agent-bio">Lorem ipsum dolor sit amet, consectetuer adipiscing elit. Aenean commodo ligula eget dolor. Aenean massa. Cum sociis natoque penatibus et magnis dis parturient montes, nascetur ridiculus mus. Donec quam felis, ultricies nec, pellentesque eu, pretium quis, sem. Nulla consequat massa quis enim. Donec pede justo, fringilla vel, aliquet nec, vulputate eget, arcu. In enim justo, rhoncus ut, imperdiet a, venenatis vitae, justo. Nullam dictum felis eu pede mollis pretium. Integer tincidunt. Cras dapibus. Vivamus elementum semper nisi</p>
<div class="abs divider"></div>

<h2 class="abs section-title proposals-title">Our Best Proposals</h2>
<div class="abs thumb" style="left:77px;top:794px"><div class="fill" role="img" aria-label="Agent meeting buyers outside a home" style="background:linear-gradient(#9cc3e4,#c8b8a0 60%,#6f8a4a)"></div></div>
<div class="abs thumb" style="left:241px;top:794px"><div class="fill" role="img" aria-label="Couple in front of their new house" style="background:linear-gradient(#c8ccd2,#b0a090 60%,#5f7f44)"></div></div>
<div class="abs thumb" style="left:406px;top:794px"><div class="fill" role="img" aria-label="Bright living room interior"></div></div>
<div class="abs thumb" style="left:570px;top:794px"><div class="fill" role="img" aria-label="Bright living room interior"></div></div>
<div class="abs thumb" style="left:77px;top:933px"><div class="fill" role="img" aria-label="Bright living room interior"></div></div>
<div class="abs thumb" style="left:241px;top:933px"><div class="fill" role="img" aria-label="Bright living room interior"></div></div>
<div class="abs thumb" style="left:406px;top:933px"><div class="fill" role="img" aria-label="Bright living room interior"></div></div>
<div class="abs thumb" style="left:570px;top:933px"><div class="fill" role="img" aria-label="Bright living room interior"></div></div>
<a class="abs btn btn-navy btn-proposals">ALL PROPOSALS</a>

<h2 class="abs section-title news-title">Latest News</h2>
<div class="abs date" style="top:794px"><span class="day">29</span><span class="mon">SEP</span></div>
<p class="abs news-text" style="top:791px">Lorem ipsum dolor sit amet, con-sectetuer adipiscing elit. Aenean commodo ligula eget dolor.</p>
<div class="abs date" style="top:894px"><span class="day">29</span><span class="mon">SEP</span></div>
<p class="abs news-text" style="top:891px">Lorem ipsum dolor sit amet, con-sectetuer adipiscing elit. Aenean commodo ligula eget dolor.</p>
<div class="abs date" style="top:994px"><span class="day">29</span><span class="mon">SEP</span></div>
<p class="abs news-text" style="top:991px">Lorem ipsum dolor sit amet, con-sectetuer adipiscing elit. Aenean commodo ligula eget dolor.</p>
<a class="abs btn btn-navy btn-news">MORE NEWS</a>

<footer class="abs site-footer"></footer>
<p class="abs copyright">Copyright © 2011 Coastline Realty. All rights reserved. Privacy Policy &nbsp;|&nbsp; Terms of Use</p>
<span class="abs social" style="left:1007px;background:#3b5c9e"></span>
<span class="abs social" style="left:1053px;background:#4fa6d8"></span>
<span class="abs social" style="left:1099px;background:#e8701e"></span>
</body>
</html>
```